Photography Studio Prep Guide Design Needed

I have a prep guide I send to all parents who book a session - It is outdated and ugly. I want a gorgeous, clean, modern upscale look for the brochure I send.

I already have the text and can provide photos for the final design. I want the cover to be clean and upscale and modern, with a happy feel.

Target Market(s)

My clients for an upscale Newborn Photography Studio

Requirements
Must have
• space for my photos, an upscale clean feel
Nice to have
• I love color, but don't want the brochure to look busy. I love cream, white, pale pink.

```html
<!DOCTYPE html>
<html lang="en">
<head>
<meta charset="utf-8">
<title>Newborn Session Prep Guide</title>
<link rel="stylesheet" href="https://fonts.googleapis.com/css2?family=Kaushan+Script&family=Open+Sans:wght@400;600;700&family=Oswald:wght@500&display=swap">
<style>
  :root {
    --board: #858585;
    --plum: #761c45;
    --plum-soft: #9b3a66;
    --ink: #3b3236;
    --paper: #ffffff;
    --cream: #f2e0d3;
    --blush: #f6dbe6;
    --blush-deep: #efc4d6;
  }
  * { margin: 0; padding: 0; box-sizing: border-box; }
  html, body { width: 1200px; height: 906px; overflow: hidden; }
  body { background: var(--board); font-family: "Open Sans", Arial, sans-serif; color: var(--ink); position: relative; }

  .page {
    position: absolute; width: 518px; height: 366px; overflow: hidden;
    background: var(--paper); box-shadow: 0 3px 10px rgba(0,0,0,.35);
  }
  .page--cover { left: 65px; top: 68px; background: linear-gradient(160deg, #f4e6dc 0%, var(--cream) 60%, #ead2c4 100%); }
  .page--intro { left: 616px; top: 68px; }
  .page--care { left: 65px; top: 468px; background: linear-gradient(180deg, #f7e3ec 0%, #fbf1f5 45%, #f4d6e3 100%); }
  .page--family { left: 616px; top: 468px; }

  .photo { position: absolute; }

  /* cover */
  .brand { position: absolute; left: 66px; top: 76px; width: 140px; text-align: center; }
  .brand-dot { width: 10px; height: 10px; border-radius: 50%; background: var(--plum); margin: 0 auto 8px; }
  .brand-name { font-family: "Open Sans", Arial, sans-serif; font-weight: 600; font-size: 13px; line-height: 1.3; color: var(--plum); letter-spacing: .5px; }
  .cover-title { position: absolute; left: 20px; width: 232px; top: 226px; text-align: center; font-family: "Kaushan Script", cursive; font-size: 19px; color: var(--plum); }
  .cover-sub { position: absolute; left: 20px; width: 232px; top: 256px; text-align: center; font-weight: 700; font-size: 11px; letter-spacing: 2px; color: #4a3e42; }
  .photo--wreath { left: 228px; top: 8px; width: 318px; height: 318px; border-radius: 50%;
    background: radial-gradient(circle at 50% 50%, #f3d7d8 0%, #eab9c2 45%, #c9a79a 62%, #7e9466 72%, #5e7a4b 100%); }

  /* common text */
  .section { position: absolute; }
  .heading { font-family: "Oswald", Arial, sans-serif; font-weight: 500; font-size: 10.5px; color: var(--plum); letter-spacing: .3px; display: flex; align-items: center; gap: 6px; margin-bottom: 6px; }
  .heading::before { content: ""; width: 3px; height: 10px; background: var(--plum); }
  .body { font-size: 6px; line-height: 1.38; }
  .body p + p { margin-top: 5px; }

  /* intro page */
  .photo--bunny { left: 0; top: 0; width: 207px; height: 366px;
    background: linear-gradient(180deg, #e8e2dc 0%, #b9aea4 35%, #7d8fc4 60%, #e9e4de 85%, #f3efea 100%); }
  .intro-title { position: absolute; left: 238px; top: 52px; font-size: 17px; font-weight: 600; line-height: 1.2; color: var(--plum); }
  .intro-lead { position: absolute; left: 238px; top: 104px; width: 230px; font-size: 6.6px; line-height: 1.35; color: var(--plum-soft); }
  .intro-nursing { left: 225px; top: 154px; width: 262px; }
  .intro-feeding { left: 225px; top: 260px; width: 262px; }

  /* care page */
  .photo--sleeper { left: 240px; top: 196px; width: 278px; height: 170px;
    background: radial-gradient(ellipse at 55% 55%, #f6dcd4 0%, #efc7cf 45%, #f4d6e3 80%); }
  .care-awake { left: 22px; top: 38px; width: 482px; }
  .care-clothes { left: 22px; top: 94px; width: 482px; }
  .care-pacifier { left: 22px; top: 141px; width: 482px; }
  .care-studio { left: 22px; top: 190px; width: 250px; }
  .care-role { left: 22px; top: 291px; width: 250px; }

  /* family page */
  .photo--sibling { left: 23px; top: 23px; width: 106px; height: 145px; background: linear-gradient(160deg, #f3e2b7 0%, #e6c9b0 60%, #d8bfae 100%); }
  .photo--mother { left: 133px; top: 23px; width: 105px; height: 145px; background: linear-gradient(160deg, #e7d6c4 0%, #d9bfa7 60%, #cdb5a1 100%); }
  .photo--parents { left: 23px; top: 173px; width: 215px; height: 175px; background: linear-gradient(160deg, #e9e4df 0%, #d2b8a6 50%, #b8a191 100%); }
  .family-time { left: 259px; top: 66px; width: 240px; }
  .family-photos { left: 259px; top: 157px; width: 240px; }
  .family-siblings { left: 259px; top: 242px; width: 240px; }
</style>
</head>
<body>

<section class="page page--cover">
  <div class="brand">
    <div class="brand-dot"></div>
    <div class="brand-name">Clara Whitfield<br>Photography</div>
  </div>
  <h1 class="cover-title">New Born Session</h1>
  <p class="cover-sub">PREP GUIDE</p>
  <div class="photo photo--wreath" role="img" aria-label="Newborn sleeping in a pink blanket inside a floral wreath basket"></div>
</section>

<section class="page page--intro">
  <div class="photo photo--bunny" role="img" aria-label="Newborn in a knitted bunny hat sleeping in a white wooden bowl on fur"></div>
  <h2 class="intro-title">Parent Instructions &amp;<br>Preparations</h2>
  <p class="intro-lead">Congratulations on expecting a baby! Here are my instructions to ensure a successful newborn photography session. Please follow these instructions as closely as possible.</p>

  <div class="section intro-nursing">
    <h3 class="heading">1. NURSING</h3>
    <div class="body">
      <p>If you are nursing, please avoid eating anything spicy (hot sauce, hot peppers, curry, etc.) that might upset baby’s tummy for 24 hours preceding your scheduled session.</p>
      <p>Please if you are breastfeeding do NOT drink caffeine or coffee before your session – I know this is hard but baby will be wired if you have caffeine.</p>
      <p>If you notice baby has a lot of gas after feedings please check with your pediatrician and bring gas drops (Tummyease or other brand) to your session. The most common reason a baby will not settle for a session is gas pressure/discomfort.</p>
    </div>
  </div>

  <div class="section intro-feeding">
    <h3 class="heading">2. FEEDING</h3>
    <div class="body">
      <p>Feed the baby as much as possible in the 24 hours preceding your session – this will help minimize the amount baby needs to feed during the session, and will help baby sleep as long and as soundly as possible. Feed baby 2-3 hours before your session and not again until you arrive. This feeding is planned in your session time and it’s not rushed. Please bring an extra bottle of formula or breastmilk to the session if possible – sometimes a small amount of milk in a bottle can quickly soothe a baby back to sleep without requiring a full feeding. I will respect your wishes if you choose not to use a bottle, but please understand we may have to pass on some poses if baby will not settle in position, and I cannot use a bottle to soothe them into the pose.</p>
    </div>
  </div>
</section>

<section class="page page--care">
  <div class="photo photo--sleeper" role="img" aria-label="Newborn asleep on pink fabric wearing a delicate leaf headband"></div>

  <div class="section care-awake">
    <h3 class="heading">3. KEEP BABY AWAKE</h3>
    <div class="body"><p>Interact with, and keep baby awake for 2 hours preceding your appointment to make sure they are nice and sleepy for their session. A great way to do this is by giving baby a bath – which will get them nice and clean and keep them awake. Also – keeping baby naked, in a diaper only is a good way to keep them awake and alert. This step is extremely important – otherwise it can take a long time to get baby to sleep, and we will have less time for photos.</p></div>
  </div>

  <div class="section care-clothes">
    <h3 class="heading">4. CLOTHES</h3>
    <div class="body"><p>Please dress baby in a simple loose sleeper we can just unsnap when you arrive – we want to keep baby as calm and happy as possible and want to avoid clothes we have to pull over their head. I provide all clothing/hats/props at your session.</p></div>
  </div>

  <div class="section care-pacifier">
    <h3 class="heading">5. PACIFIER</h3>
    <div class="body"><p>Please bring a pacifier – it can be very helpful during a session if a baby is fussy. Please note I only use the pacifier for a few minutes at a time to soothe into a pose. If you choose not to bring a pacifier I will respect your decision, but please understand we may have to pass on several poses if you do not bring one.</p></div>
  </div>

  <div class="section care-studio">
    <h3 class="heading">6. STUDIO</h3>
    <div class="body"><p>My studio is kept VERY warm to make sure your baby is comfortable through the whole session. It will be around 75-80 degrees so please dress in layers for comfort. I will have cold bottles of water available during your session. Please note – if you ask me to turn the heat down, or tell me it is too warm for baby, I cannot guarantee any results for your session. Babies are used to 98.6 degrees in the womb, and a cold studio will wake baby immediately. Babies do not wear much during their sessions and lose heat quickly. If you ask me to turn the heat down, and baby is fussy I will finish the session with only swaddled poses, or with parents. It is not safe to put an awake, alert baby in any props.</p></div>
  </div>

  <div class="section care-role">
    <h3 class="heading">7. YOUR ROLE</h3>
    <div class="body"><p>Your role at this session is to sit back and relax. I need very little assistance during the session, and want you to take this time to rest, relax and enjoy the session. Feel free to nap, catch up on work, thank you notes, or whatever you like. If baby needs to feed during the session that will be your only task! I will occasionally ask for a spotter for safety on some poses.</p></div>
  </div>
</section>

<section class="page page--family">
  <div class="photo photo--sibling" role="img" aria-label="Smiling big sister holding her newborn sibling"></div>
  <div class="photo photo--mother" role="img" aria-label="Mother kissing her newborn"></div>
  <div class="photo photo--parents" role="img" aria-label="Parents cuddling their newborn together"></div>

  <div class="section family-time">
    <h3 class="heading">8. TIME</h3>
    <div class="body"><p>Your session will last between 2-4 hours- please keep this in mind. I will provide bottled water and light snacks (granola bars/pretzels/etc.) but you may want to bring more food since the session can last up to 4 hours. Please note that I cannot shoot past 4 hours – if baby is fussy I will do my best to get beautiful photos. At 3 hours if baby is still fussy I will let you know that we need to switch to swaddled/wrapped poses to finish the session. Or we can do more family photos as well.</p></div>
  </div>

  <div class="section family-photos">
    <h3 class="heading">9. FAMILY PHOTOS/CLOTHING</h3>
    <div class="body"><p>I highly recommend mom and dad wear simple white/cream shirts, or black/navy shirts which will keep the focus on the baby. Mom can choose a tank top or dress as well. That is only a suggestion, and of course you are welcome to wear anything you choose. If dad is comfortable baring his chest it can make for some beautiful images, but that is totally up to the comfort of dad! My photos of newborns with mom/dad are generally from the waist up, so your pants or shoes will not matter.</p></div>
  </div>

  <div class="section family-siblings">
    <h3 class="heading">10. SIBLING PHOTOS</h3>
    <div class="body">
      <p>Photos of your newborn with their sibling(s) are included, and will be done at the very beginning of the session. I recommend having sibling boys wear cream/white tops or plain dark shirts with jeans. Sibling girls can wear cream/white shirts/tank tops with jeans or cream/ white dresses.</p>
      <p>I do not recommend bringing toddlers/children for the entire session. It is very hot in my studio and there is not adequate room for them to play, which makes them unhappy! Please plan to bring them for photos at the beginning of the session, and have dad or a grandparent take them out for an activity while we finish the session.</p>
    </div>
  </div>
</section>

</body>
</html>
```